Harborlane Consultants LLC web site

Harborlane Consultants LLC is a consulting and recruiting firm that provides education, perspective, guidance, and assistance to financial advisors. Dennis Malbrook is the founder of this new firm and is the only employee at this time.
Please see the attached overview which will provide much narrative describing the firm, its purpose, scope of services offered, and other useful information to help you design a web site.

Target Market(s)

US based financial advisors who are looking to transition their business to an independent ( non-employee ) business model.

Industry/Entity Type

Consultant

Coding

Coded - Design and coding required

Number of Pages Required

5+ page

Font styles to use
Sans Serif

Requirements
Must have
• all relevant pages for a basic web site : Home, About, Services offered, Contact, Resources , etc.
Nice to have
• color scheme : see logo in the attached briefing document

```html
<!DOCTYPE html>
<html lang="en">
<head>
<meta charset="utf-8">
<title>Harborlane Consultants LLC</title>
<link href="https://fonts.googleapis.com/css2?family=Cinzel:wght@400;500;600&family=Lato:wght@400;700&display=swap" rel="stylesheet">
<style>
:root{
  --navy:#0b4a7e;
  --navy-deep:#083a64;
  --grey:#6c6c6c;
  --grey-dark:#5a5a5a;
  --ink:#333;
  --muted:#555;
  --light:#f3f3f3;
  --white:#fff;
}
*{box-sizing:border-box;margin:0;padding:0}
html,body{width:1200px;height:4301px;overflow:hidden}
body{position:relative;font-family:"Lato",sans-serif;color:var(--ink);background:var(--white)}
.serif{font-family:"Cinzel",serif}
section,header,footer{position:absolute;left:0;width:1200px}
.abs{position:absolute}
.btn{position:absolute;display:flex;align-items:center;justify-content:center;border-radius:30px;font-family:"Cinzel",serif;font-size:14px;letter-spacing:.5px;background:var(--navy);color:var(--white)}
.btn.light{background:var(--white);color:var(--navy)}
.brand{font-family:"Cinzel",serif;font-weight:500;color:var(--navy);text-transform:uppercase;display:flex;align-items:center;gap:12px}
.brand-name{display:flex;flex-direction:column}
.brand-name .main{font-size:22px;line-height:22px;letter-spacing:2px}
.brand-name .sub{font-size:11px;line-height:13px;letter-spacing:2.6px}
p{line-height:1.72}

/* header */
.site-header{top:0;height:100px}
.site-header .brand{left:108px;top:28px}
.brand-dot{width:44px;height:44px;border-radius:50%;background:var(--navy)}
.nav{position:absolute;top:46px;font-size:13px;color:#222;letter-spacing:.3px}

/* hero */
.hero{top:100px;height:580px;background:linear-gradient(180deg,#8fb3d6 0%,#c6dbee 45%,#5f8fb1 62%,#8c7f5a 78%,#6f6a44 100%)}
.hero-title{position:absolute;left:108px;top:190px;font-family:"Cinzel",serif;font-weight:500;color:var(--navy)}
.hero-title .main{display:block;font-size:50px;line-height:50px;letter-spacing:4px}
.hero-title .sub{display:block;font-size:21px;line-height:26px;letter-spacing:7.5px;color:#3d4f63}
.hero .tag{position:absolute;left:108px;top:282px;font-size:12px;color:#333}

/* about */
.about{top:680px;height:660px}
.about .eyebrow{left:634px;top:148px;font-size:20px;color:var(--grey-dark)}
.about h2{position:absolute;left:634px;top:186px;font-family:"Cinzel",serif;font-weight:500;color:var(--navy);font-size:31px;letter-spacing:.5px}
.about .body{left:634px;top:250px;width:460px;font-size:12px;color:#444}
.about .body p+p{margin-top:16px}

/* services */
.services{top:1340px;height:625px}
.panel{position:absolute;color:var(--white)}
.panel.teams{left:0;top:0;width:628px;height:536px;background:linear-gradient(135deg,#1d5d91,#0b4a7e 60%,#0a3f6c)}
.panel.ria{left:564px;top:90px;width:636px;height:535px;background:linear-gradient(135deg,#8a8a8a,#6c6c6c 60%,#5e5e5e)}
.panel h3{position:absolute;font-family:"Cinzel",serif;font-weight:500;font-size:29px;line-height:46px;letter-spacing:1px}
.panel p{position:absolute;font-size:12px;line-height:1.65}

/* why */
.why{top:1965px;height:659px;background:linear-gradient(180deg,#fff 0%,#f5f8fb 70%,#eaf0f6 100%)}
.why .eyebrow{width:100%;text-align:center;top:64px;font-size:19px;color:var(--grey-dark);letter-spacing:.5px}
.why h2{position:absolute;width:100%;text-align:center;top:98px;font-family:"Cinzel",serif;font-weight:500;font-size:30px;color:var(--navy)}
.why .body{left:108px;top:208px;width:440px;font-size:12px;color:#444}
.why .body p+p{margin-top:16px}
.why a{color:var(--navy)}
.founder-name{position:absolute;left:645px;width:400px;text-align:center;top:550px;font-family:"Cinzel",serif;font-size:28px;color:var(--navy);font-weight:500;line-height:30px}
.founder-role{position:absolute;left:645px;width:400px;text-align:center;top:581px;font-family:"Cinzel",serif;font-size:18px;color:#444}

/* contact */
.contact{top:2624px;height:567px;background:linear-gradient(90deg,#6a6a6a 0%,#767676 45%,#8a8782 60%,#b7ab98 80%,#8d8477 100%)}
.contact h2{position:absolute;left:108px;top:118px;font-family:"Cinzel",serif;font-weight:500;font-size:30px;color:var(--white);letter-spacing:1px}
.field{position:absolute;background:var(--white);border:none;font-family:"Lato",sans-serif;font-size:11px;font-style:italic;color:#aaa;padding:12px 16px}

/* articles */
.articles{top:3191px;height:706px}
.articles .eyebrow{width:100%;text-align:center;top:76px;font-size:19px;color:var(--grey-dark)}
.articles h2{position:absolute;width:100%;text-align:center;top:112px;font-family:"Cinzel",serif;font-weight:500;font-size:30px;color:var(--navy)}
.card{position:absolute;top:166px;width:317px;height:412px;background:var(--light)}
.card .thumb{height:245px}
.card h4{position:absolute;left:26px;top:270px;font-family:"Cinzel",serif;font-weight:400;font-size:15px;color:#444}
.card p{position:absolute;left:30px;top:304px;width:260px;font-size:11.5px;color:#555;line-height:1.7}
.card .likes{position:absolute;left:30px;top:380px;font-size:12px;color:#444;display:flex;align-items:center;gap:12px}
.card .share{position:absolute;right:26px;top:378px}

/* footer */
.site-footer{top:3897px;height:404px;background:var(--navy);color:var(--white)}
.site-footer .brand{color:var(--white);left:108px;top:86px}
.site-footer .brand-dot{background:var(--white);width:40px;height:40px}
.f-title{position:absolute;top:96px;font-family:"Cinzel",serif;font-size:15px;letter-spacing:.5px}
.f-text{position:absolute;font-size:11.5px;line-height:1.72}
.f-list{position:absolute;font-size:11.5px;line-height:22px;list-style:none}
.f-list.info li{padding-left:16px;position:relative}
.f-list.info .u{border-bottom:1px solid #fff;display:inline-block;line-height:18px}
.copyright{position:absolute;left:0;top:356px;width:1200px;height:48px;background:var(--grey);font-size:11px;display:flex;align-items:center;justify-content:center}
</style>
</head>
<body>

<header class="site-header">
  <div class="brand abs"><span class="brand-dot"></span><span class="brand-name"><span class="main">Harborlane</span><span class="sub">Consultants LLC</span></span></div>
  <span class="nav" style="left:473px">HOME</span>
  <span class="nav" style="left:533px">ABOUT</span>
  <span class="nav" style="left:600px">SERVICES OFFERED</span>
  <span class="nav" style="left:738px">CONTACT</span>
  <span class="nav" style="left:820px">RESOURCES</span>
  <a class="btn" style="left:912px;top:30px;width:174px;height:43px">FREE CONSULTATION</a>
</header>

<section class="hero">
  <div class="abs" style="inset:0" role="img" aria-label="Coastal lighthouse on a grassy cliff above the ocean under a blue sky"></div>
  <h1 class="hero-title"><span class="main">HARBORLANE</span><span class="sub">CONSULTANTS LLC</span></h1>
  <div class="tag">"helping financial advisors to navigate their journey to independence"</div>
  <a class="btn" style="left:113px;top:318px;width:174px;height:44px">FREE CONSULTATION</a>
</section>

<section class="about">
  <div class="abs" style="left:134px;top:122px;width:416px;height:416px;border-radius:50%;background:linear-gradient(135deg,#3c5f86,#c9d5e2 55%,#f2f4f6)" role="img" aria-label="Hands reviewing financial charts on a tablet and paper"></div>
  <svg class="abs" style="left:100px;top:90px" width="500" height="500" viewBox="0 0 500 500">
    <path d="M 398 100 A 225 225 0 1 1 286 20" fill="none" stroke="#6c6c6c" stroke-width="9"/>
    <path d="M 420 90 A 240 240 0 1 1 272 2" fill="none" stroke="#0b4a7e" stroke-width="10"/>
    <circle cx="412" cy="86" r="60" fill="#0b4a7e" stroke="#fff" stroke-width="5"/>
    <text x="412" y="95" text-anchor="middle" font-family="Cinzel, serif" font-size="46" fill="#fff">35</text>
    <text x="412" y="112" text-anchor="middle" font-family="Cinzel, serif" font-size="10" fill="#fff">YEARS</text>
    <text x="412" y="124" text-anchor="middle" font-family="Cinzel, serif" font-size="10" fill="#fff">EXPERIENCE</text>
  </svg>
  <div class="abs serif eyebrow">ABOUT</div>
  <h2>HARBORLANE CONSULTANTS LLC</h2>
  <div class="abs body">
    <p>Harborlane Consultants LLC is a consulting and recruiting firm that provides education, perspective, guidance, and assistance to financial advisors. Specifically, we are focused on serving two distinct profiles of client :</p>
    <p>First, we assist financial advisors as they explore, plan, and execute their professional journey to independence. Most typically , this transition involves leaving the advisor's existing broker/dealer and either joining a new broker/dealer as an independent rep or establishing and launching a new and independent firm as a Registered Investment Advisor , or RIA. This is a complex process and requires a comprehensive , coordinated, and confidential approach towards achieving the clients' goal.</p>
  </div>
  <a class="btn" style="left:634px;top:475px;width:143px;height:40px">READ MORE</a>
</section>

<section class="services">
  <div class="panel teams" role="img" aria-label="Team meeting in a modern office, tinted blue">
    <h3 style="left:108px;top:140px">SERVICES FOR TEAMS AND<br>ADVISORS IN TRANSITION</h3>
    <p style="left:108px;top:262px;width:400px">Making any business transition is a complex undertaking . Harborlane Consultants offers a multistep , comprehensive process that addresses the following critical topics : ( each one may be considered to be a "waypoint" along the journey to independence )</p>
    <a class="btn light" style="left:117px;top:386px;width:143px;height:40px">READ MORE</a>
  </div>
  <div class="panel ria" role="img" aria-label="Business handshake over a meeting table, tinted grey">
    <h3 style="left:122px;top:126px">SERVICES FOR EXISTING<br>RIAs</h3>
    <p style="left:122px;top:248px;width:420px">Let's face it. You have a business to run. You have clients , and you have assets, both of which give you plenty to worry about. You have organic growth goals and are busy trying to achieve them. You may also have an interest in inorganic growth, whether that be from acquisitions or recruiting.</p>
    <a class="btn" style="left:122px;top:368px;width:142px;height:40px">READ MORE</a>
  </div>
</section>

<section class="why">
  <div class="abs serif eyebrow">CLIENT SERVICES | HOW WE WORK TOGETHER , WHAT TO EXPECT</div>
  <h2>WHY WORK WITH ME ?</h2>
  <div class="abs body">
    <p>In short, experience. I have spent my entire 35 year career in this industry, with the last 22 years spent in this exact endeavor... helping advisors like you to learn about, envision , and realize their dream of becoming independent advisors and business owners. My range of experience includes roles within many of the top companies in the financial services industry and includes positions in trading, institutional sales, retirement plan consulting, retail advisory, RIA custody sales, IBD regional management, executive director for business development (for a large strategic intermediary firm), and head of breakaway strategy for a large RIA custody provider.</p>
    <p>In the same way that you advise your clients against "going it alone" with respect to their investing, I would advise that you avoid going it alone with respect to making any transition to the independent advisor model. There is just so much information ( and misinformation ! ) , and the process is complex enough that expert guidance has value. Working with me will cut out the noise, streamline the process, protect your interests, and result in the most optimal decision for you.</p>
    <p>Additional details on my work history may be found here :<br><a>https://www.linkedin.com/in/dennis-malbrook-00000/</a></p>
  </div>
  <svg class="abs" style="left:615px;top:100px" width="460" height="460" viewBox="0 0 460 460">
    <path d="M 92 80 A 212 212 0 1 0 368 80" fill="none" stroke="#6c6c6c" stroke-width="9"/>
    <path d="M 74 64 A 232 232 0 1 0 386 64" fill="none" stroke="#0b4a7e" stroke-width="10"/>
  </svg>
  <div class="abs" style="left:653px;top:171px;width:384px;height:384px;border-radius:50%;background:linear-gradient(180deg,#f4f4f4 0%,#e6e6e6 50%,#2d3a4f 80%,#28344a 100%)" role="img" aria-label="Portrait of the founder, Dennis Malbrook"></div>
  <div class="abs" style="left:660px;top:538px;width:370px;height:60px;border-radius:30px;background:#fff;opacity:.9"></div>
  <div class="founder-name">DENNIS MALBROOK</div>
  <div class="founder-role">FOUNDER</div>
</section>

<section class="contact">
  <div class="abs" style="left:600px;top:0;width:600px;height:567px" role="img" aria-label="Two businessmen shaking hands across a table with a laptop"></div>
  <h2>CONTACT / CONNECT</h2>
  <div class="field" style="left:108px;top:185px;width:236px;height:42px">Full Name</div>
  <div class="field" style="left:356px;top:185px;width:235px;height:42px">Phone</div>
  <div class="field" style="left:108px;top:238px;width:483px;height:42px">E-Mail</div>
  <div class="field" style="left:108px;top:292px;width:483px;height:102px">Message</div>
  <a class="btn" style="left:108px;top:414px;width:144px;height:41px">SEND</a>
</section>

<section class="articles">
  <div class="abs serif eyebrow">OUR LATEST</div>
  <h2>ARTICLES</h2>

  <article class="card" style="left:108px">
    <div class="thumb" style="background:linear-gradient(135deg,#fafafa,#e4e4e4 70%,#2a2a2a)" role="img" aria-label="Stock market line chart on a screen"></div>
    <h4>ARTICLE TITLE #01</h4>
    <p>Lorem Ipsum is simply dummy text of the printing and typesetting industry. Lorem Ipsum has been the industry's standard dummy text.</p>
    <div class="likes"><svg width="18" height="16" viewBox="0 0 24 22"><path d="M12 21 L3 12 A5.5 5.5 0 0 1 12 4 A5.5 5.5 0 0 1 21 12 Z" fill="#e03a3a"/></svg>365</div>
    <svg class="share" width="20" height="16" viewBox="0 0 20 16"><path d="M12 1 L19 7 L12 13 V9 C6 9 3 11 1 15 C2 9 5 5 12 5 Z" fill="#c7c7c7"/></svg>
  </article>

  <article class="card" style="left:440px">
    <div class="thumb" style="background:linear-gradient(160deg,#5c6a74,#c9ccce 55%,#eef0f0)" role="img" aria-label="Person writing notes beside a laptop"></div>
    <h4>ARTICLE TITLE #02</h4>
    <p>Lorem Ipsum is simply dummy text of the printing and typesetting industry. Lorem Ipsum has been the industry's standard dummy text.</p>
    <div class="likes"><svg width="18" height="16" viewBox="0 0 24 22"><path d="M12 21 L3 12 A5.5 5.5 0 0 1 12 4 A5.5 5.5 0 0 1 21 12 Z" fill="#e03a3a"/></svg>541</div>
    <svg class="share" width="20" height="16" viewBox="0 0 20 16"><path d="M12 1 L19 7 L12 13 V9 C6 9 3 11 1 15 C2 9 5 5 12 5 Z" fill="#c7c7c7"/></svg>
  </article>

  <article class="card" style="left:769px">
    <div class="thumb" style="background:linear-gradient(135deg,#8fa596,#c9d3c6 50%,#7d8f82)" role="img" aria-label="Pile of banknotes"></div>
    <h4>ARTICLE TITLE #03</h4>
    <p>Lorem Ipsum is simply dummy text of the printing and typesetting industry. Lorem Ipsum has been the industry's standard dummy text.</p>
    <div class="likes"><svg width="18" height="16" viewBox="0 0 24 22"><path d="M12 21 L3 12 A5.5 5.5 0 0 1 12 4 A5.5 5.5 0 0 1 21 12 Z" fill="#e03a3a"/></svg>212</div>
    <svg class="share" width="20" height="16" viewBox="0 0 20 16"><path d="M12 1 L19 7 L12 13 V9 C6 9 3 11 1 15 C2 9 5 5 12 5 Z" fill="#c7c7c7"/></svg>
  </article>

  <a class="btn" style="left:504px;top:616px;width:185px;height:40px">VIEW MORE ARTICLES</a>
</section>

<footer class="site-footer">
  <div class="brand abs"><span class="brand-dot"></span><span class="brand-name"><span class="main">Harborlane</span><span class="sub">Consultants LLC</span></span></div>
  <p class="f-text" style="left:108px;top:164px;width:230px">Harborlane Consultants LLC is a consulting and recruiting firm that provides education, perspective, guidance, and assistance to financial advisors.</p>
  <a class="f-text serif" style="left:108px;top:258px;text-decoration:underline;font-size:12px">READ MORE</a>

  <div class="f-title" style="left:400px">QUICK LINKS</div>
  <ul class="f-list" style="left:400px;top:140px">
    <li>Home</li><li>About</li><li>Services offered</li><li>Contact</li><li>Resources</li>
  </ul>

  <div class="f-title" style="left:552px">CONTACT INFO</div>
  <ul class="f-list info" style="left:552px;top:140px;line-height:19.5px">
    <li><svg class="abs" style="left:2px;top:4px" width="9" height="12" viewBox="0 0 10 14"><path d="M5 0 A5 5 0 0 1 10 5 C10 9 5 14 5 14 C5 14 0 9 0 5 A5 5 0 0 1 5 0 Z" fill="#9fb7cf"/></svg>location : Cedar Bay, FL<br>N 27 degrees, 12 minutes,<br><span class="u">10.40 seconds Latitude</span><br>W 80 degrees, 44 minutes,<br><span class="u">3.20 seconds Longitude</span></li>
    <li><svg class="abs" style="left:1px;top:5px" width="10" height="10" viewBox="0 0 10 10"><path d="M2 0 L4 3 L3 4 C4 6 5 7 6 7 L7 6 L10 8 L8 10 C4 10 0 6 0 2 Z" fill="#9fb7cf"/></svg>555-201-7734</li>
    <li><svg class="abs" style="left:1px;top:6px" width="10" height="8" viewBox="0 0 10 8"><rect width="10" height="8" fill="#9fb7cf"/><path d="M0 0 L5 4 L10 0" stroke="#0b4a7e" fill="none"/></svg>dennis@harborlane-consultants.com</li>
    <li><svg class="abs" style="left:1px;top:5px" width="10" height="10" viewBox="0 0 10 10"><rect width="10" height="10" fill="#9fb7cf"/></svg>linkedin.com/in/dennis-malbrook-00000/</li>
  </ul>

  <div class="f-title" style="left:850px">NEWSLETTER</div>
  <div class="field" style="left:836px;top:159px;width:250px;height:40px;border-radius:20px;font-size:11px;padding:12px 28px">E-Mail</div>
  <a class="btn" style="left:836px;top:213px;width:134px;height:41px;background:var(--grey)">SUBSCRIBE</a>

  <div class="copyright">© 2021 Harborlane Consultants LLC | All Rights Reserved</div>
</footer>

</body>
</html>
```